Web Design Project

The client is unsure if they want a completely new design or a design that matches their existing site closely (https://www.talvoinsurance.com.au). So essentially we are looking for some designs that reflect the existing sites shape and colour and some designs that have their own new style. The company will sell three main types of insurance, Car, Bike and Caravan.

Read the complete brief and in the attached document.
The logo is also attached

I have also attached a zip of a few classic cars, if you can incorporate those.

Industry/Entity Type

Insurance

Requirements
Should not have

```html
<!DOCTYPE html>
<html lang="en">
<head>
<meta charset="utf-8">
<title>Talvo Insurance – Insure with an Enthusiast</title>
<link rel="stylesheet" href="https://fonts.googleapis.com/css2?family=Source+Sans+3:wght@300;400;600;700&family=Arimo:wght@400;700&family=Kaushan+Script&display=swap">
<style>
  :root {
    --bg: #141414;
    --bg-soft: #1f1f1f;
    --panel: #2b2b2b;
    --panel-edge: #4a4a4a;
    --red: #c4161c;
    --red-dark: #9e1015;
    --red-text: #d8121a;
    --white: #ffffff;
    --grey-text: #8d8d8d;
    --grey-line: #3a3a3a;
    --divider: #050505;
  }
  * { box-sizing: border-box; margin: 0; padding: 0; }
  html, body { width: 1200px; height: 900px; overflow: hidden; }
  body {
    position: relative;
    background:
      radial-gradient(ellipse 520px 300px at 950px 620px, rgba(70,70,70,.35), transparent 70%),
      radial-gradient(ellipse 500px 260px at 180px 200px, rgba(60,60,60,.35), transparent 70%),
      linear-gradient(180deg, #1a1a1a 0%, var(--bg) 100%);
    color: var(--white);
    font-family: "Source Sans 3", sans-serif;
  }
  .abs { position: absolute; }
  .top-rule { left: 0; top: 0; width: 1200px; height: 4px; background: var(--red); }

  /* Header */
  .brand { left: 113px; top: 28px; width: 190px; height: 67px; display: flex; align-items: center; gap: 10px; }
  .brand-dot { width: 14px; height: 14px; border-radius: 50%; background: #c9c9c9; flex: none; }
  .brand-name { font-family: "Arimo", sans-serif; font-weight: 700; font-size: 19px; color: #e2e2e2; letter-spacing: .5px; line-height: 1.05; }
  .tagline { left: 405px; top: 16px; font-weight: 700; font-size: 24px; letter-spacing: .2px; }
  .phone { left: 474px; top: 44px; font-size: 22px; color: var(--red-text); font-weight: 400; letter-spacing: .5px; }
  .account { right: 113px; top: 9px; font-family: "Arimo", sans-serif; font-size: 12px; color: #cfcfcf; }
  .account .sep { margin: 0 10px; }
  .follow { left: 838px; top: 50px; font-family: "Kaushan Script", cursive; font-size: 20px; color: #d8d8d8; }
  .social { left: 958px; top: 50px; display: flex; gap: 6px; }
  .social span { width: 30px; height: 30px; border-radius: 50%; background: #5a5a5a; }

  /* Navigation */
  .nav { left: 469px; top: 106px; display: flex; font-family: "Arimo", sans-serif; font-size: 14px; }
  .nav a { color: var(--white); text-decoration: none; height: 26px; line-height: 26px; text-align: center; }
  .nav a.active { background: var(--red); border-radius: 5px; }

  /* Hero */
  .hero { left: 104px; top: 142px; width: 994px; height: 353px; background: linear-gradient(180deg, #303030, #262626); border: 1px solid var(--panel-edge); }
  .hero-photo { left: 115px; top: 155px; width: 668px; height: 328px; background: radial-gradient(ellipse at 60% 45%, #d9c36a 0%, #a99552 30%, #8e8e8e 55%, #e4e4e4 100%); }
  .news { left: 115px; top: 405px; width: 668px; height: 78px; background: rgba(70,70,70,.85); padding: 6px 10px 0 8px; }
  .news h2 { font-family: "Source Sans 3", sans-serif; font-weight: 600; font-size: 22px; line-height: 28px; }
  .news h2 em, .section-title em { font-style: normal; color: var(--red-text); }
  .news p { font-family: "Arimo", sans-serif; font-size: 11px; line-height: 16px; margin: 4px 0 0 4px; color: #eee; }

  .pitch { left: 807px; top: 162px; width: 285px; font-family: "Arimo", sans-serif; font-weight: 700; font-size: 17px; line-height: 30px; }
  .pitch .red { color: var(--red-text); }
  .pitch .needs { font-size: 19px; letter-spacing: .5px; }
  .benefits { left: 807px; top: 259px; list-style: none; font-family: "Arimo", sans-serif; font-size: 13px; }
  .benefits li { height: 20px; line-height: 20px; display: flex; align-items: center; gap: 8px; }
  .benefits svg { width: 14px; height: 12px; flex: none; }
  .pay { left: 824px; top: 430px; width: 211px; height: 37px; border-radius: 10px; background: linear-gradient(180deg, #e0262c, var(--red-dark)); border: 1px solid #e9555a; display: flex; align-items: center; justify-content: space-between; padding: 0 10px 0 16px; font-family: "Arimo", sans-serif; font-weight: 700; font-size: 18px; color: var(--white); text-decoration: none; }
  .pay svg { width: 22px; height: 22px; }

  /* Sections */
  .section-title { font-weight: 400; font-size: 24px; letter-spacing: .2px; text-transform: uppercase; }
  .about-title { left: 117px; top: 539px; }
  .events-title { left: 447px; top: 539px; }
  .aff-title { left: 788px; top: 539px; }
  .divider { top: 540px; width: 1px; height: 295px; background: var(--divider); box-shadow: 1px 0 0 #2a2a2a; }

  .about-frame { left: 108px; top: 587px; width: 276px; height: 148px; background: #5a5a5a; border: 1px solid #777; }
  .about-photo { left: 115px; top: 594px; width: 262px; height: 133px; background: radial-gradient(ellipse at 50% 55%, #b3272b 0%, #8d8d8d 45%, #ececec 100%); }
  .about-text { left: 109px; top: 746px; width: 276px; font-size: 13px; line-height: 20px; color: var(--grey-text); }
  .view-detail { left: 303px; top: 820px; display: flex; align-items: center; gap: 5px; font-size: 13px; color: var(--red-text); text-decoration: underline; }
  .view-detail svg { width: 12px; height: 12px; }

  .event { left: 437px; width: 290px; }
  .event-head { display: flex; align-items: center; font-weight: 700; font-size: 12.5px; color: var(--white); }
  .event-head svg { width: 10px; height: 8px; margin-right: 7px; }
  .event-head time { margin-left: auto; }
  .event p { margin: 3px 0 0 17px; width: 266px; font-size: 12.5px; line-height: 16px; color: #6f6f6f; text-align: justify; }
  .event-rule { left: 454px; width: 266px; height: 1px; background: var(--grey-line); }

  .badge { background: var(--white); }

  /* Footer */
  .footer { left: 0; top: 862px; width: 1200px; height: 38px; background: #b81c1f; font-family: "Arimo", sans-serif; font-size: 12.5px; display: flex; align-items: center; justify-content: space-between; padding: 0 110px; }
  .footer nav a { color: var(--white); text-decoration: none; }
  .footer nav .sep { margin: 0 9px; }
</style>
</head>
<body>
  <div class="abs top-rule"></div>

  <header>
    <div class="abs brand"><span class="brand-dot"></span><span class="brand-name">TALVO<br>INSURANCE</span></div>
    <div class="abs tagline">Insure with an Enthusiast</div>
    <div class="abs phone">1300 482 915</div>
    <div class="abs account">Broker Login<span class="sep">|</span>register</div>
    <div class="abs follow">Follow us on</div>
    <div class="abs social" aria-label="Social links"><span></span><span></span><span></span><span></span></div>
    <nav class="abs nav">
      <a class="active" href="#" style="width:86px">About Us</a>
      <a href="#" style="width:114px">Insurance</a>
      <a href="#" style="width:86px">Events</a>
      <a href="#" style="width:88px">Clubs</a>
      <a href="#" style="width:92px">Links</a>
      <a href="#" style="width:64px">FAQ</a>
      <a href="#" style="width:130px">Contact Us</a>
    </nav>
  </header>

  <section>
    <div class="abs hero"></div>
    <div class="abs hero-photo" role="img" aria-label="Yellow vintage open-top roadster in a studio"></div>
    <div class="abs news">
      <h2>News on All Things <em>MOTORING</em></h2>
      <p>In almost 50 years, the expectations were high on the latest offering from the Veloce sportscar. It has taken almost 50 years, Veloce has pushed themselves to satisfy even the harshest of critics to offer what is being hailed as "the best V9 yet"</p>
    </div>
    <div class="abs pitch">
      The specialised <span class="red">CAR INSURANCE</span><br>
      cover your Classic or Prestige car<br>
      <span class="red needs">NEEDS</span>
    </div>
    <ul class="abs benefits">
      <li><svg viewBox="0 0 14 12"><path d="M1 6l4 4 8-9" fill="none" stroke="#d8121a" stroke-width="2.4"/></svg>Agreed Value</li>
      <li><svg viewBox="0 0 14 12"><path d="M1 6l4 4 8-9" fill="none" stroke="#d8121a" stroke-width="2.4"/></svg>New Replacement Vehicle in first 2 years</li>
      <li><svg viewBox="0 0 14 12"><path d="M1 6l4 4 8-9" fill="none" stroke="#d8121a" stroke-width="2.4"/></svg>Choice of Repairer</li>
      <li><svg viewBox="0 0 14 12"><path d="M1 6l4 4 8-9" fill="none" stroke="#d8121a" stroke-width="2.4"/></svg>Lifetime Guarantee for Repairs</li>
      <li><svg viewBox="0 0 14 12"><path d="M1 6l4 4 8-9" fill="none" stroke="#d8121a" stroke-width="2.4"/></svg>Free Windscreen/Glass Benefit</li>
      <li><svg viewBox="0 0 14 12"><path d="M1 6l4 4 8-9" fill="none" stroke="#d8121a" stroke-width="2.4"/></svg>Hire car following accident or theft</li>
      <li><svg viewBox="0 0 14 12"><path d="M1 6l4 4 8-9" fill="none" stroke="#d8121a" stroke-width="2.4"/></svg>Flexible coverage</li>
    </ul>
    <a class="abs pay" href="#">Make A Payment
      <svg viewBox="0 0 22 22"><circle cx="11" cy="11" r="10" fill="#e6e6e6" stroke="#999"/><path d="M9 6l6 5-6 5z" fill="#555"/></svg>
    </a>
  </section>

  <section>
    <h3 class="abs section-title about-title">About <em>Company</em></h3>
    <div class="abs about-frame"></div>
    <div class="abs about-photo" role="img" aria-label="Red classic coupe in a studio"></div>
    <p class="abs about-text">Lorem ipsum dolor sit amet, eleifend ac proin vel erat. Id bibendum ut fringilla lobortis sed, sollici-tudin lacinia mauris...</p>
    <a class="abs view-detail" href="#">view detail
      <svg viewBox="0 0 12 12"><circle cx="6" cy="6" r="5" fill="none" stroke="#999"/><path d="M5 3.5l3 2.5-3 2.5z" fill="#999"/></svg>
    </a>
  </section>

  <div class="abs divider" style="left:412px"></div>

  <section>
    <h3 class="abs section-title events-title">Upcoming <em>Events</em></h3>
    <article class="abs event" style="top:586px">
      <div class="event-head"><svg viewBox="0 0 10 8"><path d="M0 0l4 4-4 4M5 0l4 4-4 4" fill="none" stroke="#bbb" stroke-width="1.3"/></svg>7th Annual Car and Bike Show<time>Dt. 01/12/11</time></div>
      <p>Wisi vestibulum risus sit egestas nec, nulla augue rhoncus felis elementum pede ac, nibh erat.</p>
    </article>
    <div class="abs event-rule" style="top:658px"></div>
    <article class="abs event" style="top:673px">
      <div class="event-head"><svg viewBox="0 0 10 8"><path d="M0 0l4 4-4 4M5 0l4 4-4 4" fill="none" stroke="#bbb" stroke-width="1.3"/></svg>7th Annual Car and Bike Show<time>Dt. 01/12/11</time></div>
      <p>Wisi vestibulum risus sit egestas nec, nulla augue rhoncus felis elementum pede ac, nibh erat.</p>
    </article>
    <div class="abs event-rule" style="top:746px"></div>
    <article class="abs event" style="top:760px">
      <div class="event-head"><svg viewBox="0 0 10 8"><path d="M0 0l4 4-4 4M5 0l4 4-4 4" fill="none" stroke="#bbb" stroke-width="1.3"/></svg>7th Annual Car and Bike Show<time>Dt. 01/12/11</time></div>
      <p>Wisi vestibulum risus sit egestas nec, nulla augue rhoncus felis elementum pede ac, nibh erat.</p>
    </article>
  </section>

  <div class="abs divider" style="left:753px"></div>

  <section>
    <h3 class="abs section-title aff-title">Our <em>Affiliation</em></h3>
    <div class="abs badge" style="left:790px;top:595px;width:127px;height:58px"></div>
    <div class="abs badge" style="left:946px;top:595px;width:124px;height:58px"></div>
    <div class="abs badge" style="left:791px;top:675px;width:121px;height:59px"></div>
    <div class="abs badge" style="left:964px;top:675px;width:75px;height:59px"></div>
    <div class="abs badge" style="left:799px;top:762px;width:116px;height:58px"></div>
    <div class="abs badge" style="left:936px;top:759px;width:86px;height:58px"></div>
  </section>

  <footer class="abs footer">
    <nav>
      <a href="#">Home</a><span class="sep">|</span><a href="#">About Us</a><span class="sep">|</span><a href="#">Insurance</a><span class="sep">|</span><a href="#">Events</a><span class="sep">|</span><a href="#">Clubs</a><span class="sep">|</span><a href="#">Links</a><span class="sep">|</span><a href="#">FAQ</a><span class="sep">|</span><a href="#">Contact Us</a>
    </nav>
    <span>Copyright © 2013 - TALVO - All Rights Reserved</span>
  </footer>
</body>
</html>
```